Renewable energy website needs a wordpress website

We are a Renewable Energy company specialising in Energy Management, LED Lights and Solar PV Systems based in Kuala Lumpur.
We need wordpress website designed to match our company identity.
We would like to stick with similar shades of blue & green as our logo and to keep it fresh and creative at the same time.

It Company

```html
<!DOCTYPE html>
<html lang="en">
<head>
<meta charset="utf-8">
<title>Brightfield Energy</title>
<link href="https://fonts.googleapis.com/css2?family=Open+Sans:wght@400;600;700&display=swap" rel="stylesheet">
<style>
  :root {
    --page-bg: #eceeef;
    --blue: #1a8fc4;
    --blue-deep: #0f6d9c;
    --blue-band: #1f93bd;
    --blue-band-dark: #167ba3;
    --green: #7bb52a;
    --green-dark: #5f9a1c;
    --footer: #1b6d8a;
    --footer-dark: #155a73;
    --text: #555b60;
    --text-light: #8a9196;
    --white: #ffffff;
  }
  * { box-sizing: border-box; margin: 0; padding: 0; }
  html, body { width: 1200px; height: 2300px; overflow: hidden; }
  body {
    position: relative;
    font-family: "Open Sans", Arial, sans-serif;
    color: var(--text);
    background: linear-gradient(#f6f7f7, var(--page-bg) 600px, #f3f4f4);
  }
  .abs { position: absolute; }

  /* Header */
  .brand { left: 90px; top: 34px; display: flex; align-items: center; gap: 14px; }
  .brand-dot { width: 46px; height: 46px; border-radius: 50%; background: var(--green); }
  .brand-name { font-size: 28px; font-weight: 700; color: var(--blue); letter-spacing: 1px; }
  .social { right: 84px; top: 34px; display: flex; gap: 8px; }
  .social span { width: 28px; height: 28px; border-radius: 50%; background: var(--blue); }
  .social span:nth-child(4) { background: #e38b2a; }
  .callout { right: 84px; top: 78px; text-align: right; }
  .callout-label { font-size: 14px; font-weight: 700; color: var(--green); display: flex; align-items: center; gap: 6px; justify-content: flex-end; }
  .callout-number { font-size: 22px; font-weight: 700; color: var(--blue); }

  /* Navigation */
  .main-nav {
    left: 80px; top: 168px; width: 1040px; height: 36px;
    background: linear-gradient(#8cc63a, var(--green-dark));
    display: flex; align-items: center; padding: 0 26px;
  }
  .main-nav a { color: var(--white); font-size: 13px; font-weight: 600; text-decoration: none; margin-right: 46px; text-transform: uppercase; }
  .search { margin-left: auto; width: 150px; height: 22px; border-radius: 11px; background: var(--white); font-size: 11px; color: var(--text-light); padding: 3px 12px; position: relative; }
  .search svg { position: absolute; right: 8px; top: 4px; }

  /* Hero */
  .hero {
    left: 80px; top: 204px; width: 1040px; height: 270px;
    background: linear-gradient(135deg, #2aa8dc, var(--blue-deep));
    overflow: hidden;
  }
  .hero-image { position: absolute; left: 0; top: 0; width: 520px; height: 270px;
    background: radial-gradient(circle at 55% 55%, #8dd06a 0, #4cae4a 18%, #bfe3f2 38%, #eaf6fb 70%); }
  .hero-copy { position: absolute; left: 560px; top: 44px; width: 440px; color: var(--white); }
  .hero-title { font-size: 26px; font-weight: 700; letter-spacing: 1px; margin-bottom: 14px; }
  .hero-text { font-size: 14px; line-height: 22px; opacity: .92; }
  .hero-dots { position: absolute; left: 560px; bottom: 22px; display: flex; gap: 8px; }
  .hero-dots span { width: 10px; height: 10px; border-radius: 50%; background: rgba(255,255,255,.5); }
  .hero-dots span:first-child { background: var(--white); }

  /* Section headings */
  .section-title { left: 0; width: 1200px; text-align: center; font-size: 24px; font-weight: 700; }
  .section-title .first { color: var(--blue); }
  .section-title .second { color: var(--green); }
  .drop { left: 588px; }

  /* Services */
  .service { top: 624px; width: 300px; }
  .service-image { height: 140px; }
  .service-title { margin-top: 10px; font-size: 14px; font-weight: 700; color: var(--blue); text-transform: uppercase; }
  .service-text { font-size: 13px; line-height: 19px; margin-top: 4px; }
  .read-more { font-size: 12px; color: var(--blue); font-weight: 600; margin-top: 4px; }

  /* Who we are */
  .about-band {
    left: 0; top: 940px; width: 1200px; height: 450px;
    background: linear-gradient(var(--blue-band), var(--blue-band-dark));
  }
  .about-band-top { position: absolute; left: 0; top: 0; width: 1200px; height: 70px; background: rgba(255,255,255,.12); }
  .about-title { position: absolute; top: 18px; width: 1200px; text-align: center; color: var(--white); font-size: 22px; font-weight: 700; letter-spacing: 2px; }
  .about-text { position: absolute; left: 200px; width: 800px; top: 100px; text-align: center; color: var(--white); font-size: 13px; line-height: 21px; opacity: .92; }
  .pillar { position: absolute; top: 176px; width: 200px; text-align: center; }
  .pillar-ring { width: 136px; height: 136px; margin: 0 auto; border-radius: 50%; background: var(--white); padding: 12px; }
  .pillar-core { width: 112px; height: 112px; border-radius: 50%; background: linear-gradient(#8cc63a, var(--green-dark)); display: flex; align-items: center; justify-content: center; }
  .pillar-label { margin-top: 14px; color: var(--white); font-size: 12px; font-weight: 700; text-transform: uppercase; }

  /* FAQ */
  .faq-title { left: 80px; top: 1436px; font-size: 24px; font-weight: 600; color: var(--blue); }
  .faq-item { width: 470px; display: flex; gap: 12px; }
  .faq-item svg { flex: none; margin-top: 2px; }
  .faq-q { font-size: 13px; color: var(--blue); font-weight: 600; line-height: 20px; }
  .faq-a { font-size: 13px; line-height: 20px; margin-top: 4px; }

  /* Footer */
  .footer { left: 0; top: 1830px; width: 1200px; height: 440px; background: linear-gradient(var(--footer), var(--footer-dark)); color: var(--white); }
  .footer-heading { font-size: 18px; font-weight: 600; text-transform: uppercase; }
  .contact-form { position: absolute; left: 110px; top: 24px; width: 250px; }
  .field { background: var(--white); color: var(--text-light); font-size: 12px; height: 30px; padding: 6px 10px; margin-top: 14px; border-radius: 2px; }
  .field.tall { height: 92px; }
  .send { margin-top: 14px; display: inline-block; background: var(--green); color: var(--white); font-size: 12px; font-weight: 600; padding: 7px 18px; text-transform: uppercase; }
  .footer-brand { position: absolute; left: 470px; top: 150px; width: 260px; text-align: center; }
  .footer-brand .brand-dot { margin: 0 auto 10px; width: 70px; height: 70px; }
  .footer-brand .brand-name { color: var(--white); font-size: 22px; }
  .footer-brand .social { position: static; justify-content: center; margin-top: 16px; }
  .footer-brand .social span { background: rgba(255,255,255,.85); }
  .footer-list { position: absolute; top: 24px; }
  .footer-list ul { list-style: none; margin-top: 12px; }
  .footer-list li { font-size: 13px; line-height: 22px; }
  .footer-list li::before { content: "› "; }
  .copyright { left: 0; top: 2270px; width: 1200px; height: 30px; background: var(--green); color: var(--white); font-size: 11px; text-align: center; line-height: 30px; }
</style>
</head>
<body>

<header>
  <div class="abs brand"><span class="brand-dot"></span><span class="brand-name">BRIGHTFIELD ENERGY</span></div>
  <div class="abs social" aria-label="Social links"><span></span><span></span><span></span><span></span></div>
  <div class="abs callout">
    <div class="callout-label">
      <svg width="14" height="14" viewBox="0 0 24 24"><path d="M6.6 10.8a15 15 0 006.6 6.6l2.2-2.2a1 1 0 011-.25 11.4 11.4 0 003.6.57 1 1 0 011 1V20a1 1 0 01-1 1A17 17 0 013 4a1 1 0 011-1h3.5a1 1 0 011 1c0 1.25.2 2.45.57 3.6a1 1 0 01-.25 1z" fill="#7bb52a"/></svg>
      CALL US NOW
    </div>
    <div class="callout-number">03 5550 0142</div>
  </div>
</header>

<nav class="abs main-nav">
  <a>Home</a><a>About Us</a><a>Our Services</a><a>Our Products</a><a>Technologies</a><a>Contact Us</a>
  <div class="search">Search
    <svg width="12" height="12" viewBox="0 0 24 24"><circle cx="10" cy="10" r="7" stroke="#7bb52a" stroke-width="3" fill="none"/><path d="M15 15l6 6" stroke="#7bb52a" stroke-width="3"/></svg>
  </div>
</nav>

<section class="abs hero">
  <div class="hero-image" role="img" aria-label="Hands holding a small green globe with solar panels, wind turbines and city towers"></div>
  <div class="hero-copy">
    <h1 class="hero-title">BRIGHTFIELD ENERGY</h1>
    <p class="hero-text">Clean power for homes and businesses. We plan, install and maintain solar systems, efficient lighting and smart energy controls that lower bills and cut carbon every single day.</p>
  </div>
  <div class="hero-dots"><span></span><span></span><span></span></div>
</section>

<h2 class="abs section-title" style="top:520px"><span class="first">OUR</span> <span class="second">SERVICES</span></h2>
<svg class="abs drop" style="top:560px" width="24" height="30" viewBox="0 0 24 30"><path d="M12 2C12 2 3 14 3 20a9 9 0 0018 0C21 14 12 2 12 2z" fill="#1a8fc4"/><path d="M12 12c0 0-4 5-4 8a4 4 0 008 0c0-3-4-8-4-8z" fill="#7bb52a"/></svg>

<article class="abs service" style="left:90px">
  <div class="service-image" role="img" aria-label="Worker installing solar panels on a house roof" style="background:linear-gradient(#6f8d9c,#3d5866)"></div>
  <h3 class="service-title">Residential Solar Power</h3>
  <p class="service-text">Rooftop panels sized for your home, with monitoring and upkeep included.</p>
  <p class="read-more">Read more »</p>
</article>
<article class="abs service" style="left:450px">
  <div class="service-image" role="img" aria-label="Rows of solar panels on a commercial roof under trees" style="background:linear-gradient(#8aa080,#3f5560)"></div>
  <h3 class="service-title">Commercial Solar Power</h3>
  <p class="service-text">Larger arrays for offices and factories, built to trim peak demand costs.</p>
  <p class="read-more">Read more »</p>
</article>
<article class="abs service" style="left:810px">
  <div class="service-image" role="img" aria-label="Rows of glowing LED light bulbs in blue light" style="background:linear-gradient(#2b5fb8,#0d2a66)"></div>
  <h3 class="service-title">LED Lighting</h3>
  <p class="service-text">Efficient LED fittings that use less power and last for many years.</p>
  <p class="read-more">Read more »</p>
</article>

<section class="abs about-band">
  <div class="about-band-top"></div>
  <h2 class="about-title">WHO WE ARE</h2>
  <svg style="position:absolute;left:588px;top:56px" width="24" height="30" viewBox="0 0 24 30"><path d="M12 2C12 2 3 14 3 20a9 9 0 0018 0C21 14 12 2 12 2z" fill="#ffffff"/><path d="M12 12c0 0-4 5-4 8a4 4 0 008 0c0-3-4-8-4-8z" fill="#7bb52a"/></svg>
  <p class="about-text">We are a clean energy team based in the city, helping clients manage power wisely. Our engineers combine solar generation, efficient lighting and careful monitoring to deliver lasting savings for every site we serve.</p>

  <div class="pillar" style="left:250px">
    <div class="pillar-ring"><div class="pillar-core">
      <svg width="60" height="50" viewBox="0 0 60 50" fill="#fff"><circle cx="30" cy="14" r="9"/><path d="M14 46a16 16 0 0132 0z"/><circle cx="12" cy="20" r="6"/><path d="M0 44a12 12 0 0118-10v10z"/><circle cx="48" cy="20" r="6"/><path d="M60 44a12 12 0 00-18-10v10z"/></svg>
    </div></div>
    <div class="pillar-label">About Us</div>
  </div>
  <div class="pillar" style="left:500px">
    <div class="pillar-ring"><div class="pillar-core">
      <svg width="56" height="56" viewBox="0 0 56 56" fill="#fff"><rect x="24" y="2" width="8" height="52" rx="4" transform="rotate(45 28 28)"/><rect x="24" y="2" width="8" height="52" rx="4" transform="rotate(-45 28 28)"/><circle cx="10" cy="10" r="8"/></svg>
    </div></div>
    <div class="pillar-label">Our Products</div>
  </div>
  <div class="pillar" style="left:750px">
    <div class="pillar-ring"><div class="pillar-core">
      <svg width="56" height="56" viewBox="0 0 56 56"><circle cx="28" cy="28" r="16" fill="none" stroke="#fff" stroke-width="8" stroke-dasharray="8 4"/><circle cx="28" cy="28" r="6" fill="#fff"/></svg>
    </div></div>
    <div class="pillar-label">Our Technologies</div>
  </div>
</section>

<h2 class="abs faq-title">Frequently Asked Questions</h2>
<div class="abs faq-item" style="left:90px;top:1500px">
  <svg width="16" height="16" viewBox="0 0 16 16"><path d="M2 2h12v9H7l-4 3v-3H2z" fill="#1a8fc4"/></svg>
  <div><p class="faq-q">How long does a solar system take to install?</p><p class="faq-a">Most home systems are fitted within two days once permits are approved.</p></div>
</div>
<div class="abs faq-item" style="left:630px;top:1500px">
  <svg width="16" height="16" viewBox="0 0 16 16"><path d="M2 2h12v9H7l-4 3v-3H2z" fill="#1a8fc4"/></svg>
  <div><p class="faq-q">Will panels work on cloudy days?</p><p class="faq-a">Yes, output drops a little but panels still produce useful power all year.</p></div>
</div>
<div class="abs faq-item" style="left:90px;top:1640px">
  <svg width="16" height="16" viewBox="0 0 16 16"><path d="M2 2h12v9H7l-4 3v-3H2z" fill="#1a8fc4"/></svg>
  <div><p class="faq-q">Do LED lights really save money?</p><p class="faq-a">LED fittings use far less energy and need replacing much less often.</p></div>
</div>
<div class="abs faq-item" style="left:630px;top:1640px">
  <svg width="16" height="16" viewBox="0 0 16 16"><path d="M2 2h12v9H7l-4 3v-3H2z" fill="#1a8fc4"/></svg>
  <div><p class="faq-q">Can you monitor my energy use?</p><p class="faq-a">Our monitoring service tracks usage and flags waste so you can act early.</p></div>
</div>

<footer class="abs footer">
  <div class="contact-form">
    <h3 class="footer-heading">Quick Contact</h3>
    <div class="field">Name</div>
    <div class="field">Email</div>
    <div class="field tall">Message</div>
    <div class="send">Send Message</div>
  </div>
  <div class="footer-brand">
    <span class="brand-dot" style="display:block"></span>
    <span class="brand-name">BRIGHTFIELD ENERGY</span>
    <div class="social"><span></span><span></span><span></span><span></span></div>
  </div>
  <div class="footer-list" style="left:770px">
    <h3 class="footer-heading">Navigation</h3>
    <ul><li>Home</li><li>About Us</li><li>Our Services</li><li>Our Products</li><li>Our Technologies</li><li>Contact Us</li></ul>
  </div>
  <div class="footer-list" style="left:960px">
    <h3 class="footer-heading">Useful Links</h3>
    <ul><li>SITEMAP</li><li>PRIVACY POLICY</li><li>TERMS &amp; USAGE</li></ul>
  </div>
</footer>
<div class="abs copyright">Copyright © 2015. Brightfield Energy. All Rights Reserved.</div>

</body>
</html>
```